Business card for IT company

Looking for a business card for an IT company providing server, network, and application support to medium businesses. Company name is Halvern Systems. Website is www.halvernsystems.example, would like to use the green color that is on the homepage. Prefer design to be done in Illustrator. Please, only DESIGNERS apply - no PHP programmers attempting to do design. Thank you

Industry/Entity Type

Information Technology

Requirements
Must have
• Green
Should not have
• Template designs, or designs done by non-designer type people

```html
<!DOCTYPE html>
<html lang="en">
<head>
<meta charset="utf-8">
<title>Halvern Systems – Business Card</title>
<link rel="stylesheet" href="https://fonts.googleapis.com/css2?family=Montserrat:wght@400;500;600;700&display=swap">
<style>
  :root {
    --page: #ffffff;
    --card: #3b3b3c;
    --card-deep: #333334;
    --green: #5a7a1c;
    --green-soft: rgba(90, 122, 28, 0.55);
    --ink: #ffffff;
    --ink-soft: #e9e9e9;
  }
  * { box-sizing: border-box; margin: 0; padding: 0; }
  html, body {
    width: 1200px; height: 1200px; overflow: hidden;
    background: var(--page);
    font-family: "Montserrat", sans-serif;
    color: var(--ink);
  }
  .canvas { position: relative; width: 1200px; height: 1200px; }

  .card {
    position: absolute;
    background: var(--card);
    overflow: hidden;
  }
  .card--front { left: 226px; top: 80px; width: 718px; height: 420px; }
  .card--back  { left: 254px; top: 680px; width: 720px; height: 424px; }

  .card__pattern {
    position: absolute; inset: 0;
  }
  .card--front .card__pattern {
    background:
      radial-gradient(ellipse 260px 200px at 200px 300px, var(--green-soft), transparent 70%),
      radial-gradient(ellipse 180px 140px at 390px 40px, rgba(90,122,28,0.3), transparent 70%),
      linear-gradient(180deg, transparent 60%, var(--card-deep));
  }
  .card--back .card__pattern {
    background:
      radial-gradient(ellipse 300px 200px at 200px 90px, var(--green-soft), transparent 70%),
      radial-gradient(ellipse 120px 90px at 390px 380px, rgba(90,122,28,0.35), transparent 70%),
      linear-gradient(180deg, transparent 55%, var(--card-deep));
  }

  .brand-mark {
    position: absolute;
    width: 152px; height: 152px;
    border-radius: 50%;
    background: var(--ink);
  }
  .card--front .brand-mark { left: 290px; top: 76px; }

  .wordmark {
    position: absolute;
    font-weight: 400;
    color: var(--ink);
    text-transform: uppercase;
    line-height: 1;
  }
  .wordmark__name { display: block; font-size: 40px; letter-spacing: 1px; }
  .wordmark__sub  { display: block; font-size: 22px; letter-spacing: 2px; text-align: right; margin-top: 6px; }
  .card--front .wordmark { left: 236px; top: 250px; }
  .card--back  .wordmark { left: 32px; top: 18px; }

  .person {
    position: absolute; left: 20px; top: 266px; width: 200px;
    text-align: center;
  }
  .person__avatar {
    display: block; width: 56px; height: 56px; margin: 0 auto 14px;
    border-radius: 50%; background: var(--ink);
  }
  .person__name { font-size: 27px; font-weight: 600; line-height: 1.1; }
  .person__role { font-size: 21px; font-weight: 600; margin-top: 4px; }

  .contact {
    position: absolute; right: 30px;
    display: flex; align-items: center; gap: 12px;
    font-size: 19px; font-weight: 500; color: var(--ink-soft);
    text-align: right; line-height: 1.25;
  }
  .contact__icon { width: 28px; height: 28px; flex: none; }
  .contact--address { top: 136px; }
  .contact--phone   { top: 208px; }
  .contact--web     { top: 272px; }
  .contact--email   { top: 346px; }
</style>
</head>
<body>
<main class="canvas">

  <section class="card card--front" aria-label="Card front">
    <div class="card__pattern" role="img" aria-label="Soft green tiled backdrop"></div>
    <span class="brand-mark" aria-hidden="true"></span>
    <div class="wordmark">
      <span class="wordmark__name">Halvern</span>
      <span class="wordmark__sub">Systems</span>
    </div>
  </section>

  <section class="card card--back" aria-label="Card back">
    <div class="card__pattern" role="img" aria-label="Soft green tiled backdrop"></div>
    <div class="wordmark">
      <span class="wordmark__name">Halvern</span>
      <span class="wordmark__sub">Systems</span>
    </div>

    <div class="person">
      <span class="person__avatar" role="img" aria-label="Profile photo placeholder"></span>
      <p class="person__name">YOUR NAME</p>
      <p class="person__role">Designation</p>
    </div>

    <div class="contact contact--address">
      <span>Your City Address<br>Street Location, Your City</span>
      <svg class="contact__icon" viewBox="0 0 24 24" aria-hidden="true">
        <path d="M3 12 L12 4 L21 12 H18 V20 H6 V12 Z" fill="#fff"/>
        <rect x="10" y="14" width="4" height="6" fill="#3b3b3c"/>
      </svg>
    </div>

    <div class="contact contact--phone">
      <span>+123 456 7890</span>
      <svg class="contact__icon" viewBox="0 0 24 24" aria-hidden="true">
        <rect x="7" y="2" width="10" height="20" rx="2" fill="#fff"/>
        <rect x="8.5" y="5" width="7" height="12" fill="#3b3b3c"/>
        <circle cx="12" cy="19.5" r="1" fill="#3b3b3c"/>
      </svg>
    </div>

    <div class="contact contact--web">
      <span>www.halvernsystems.example</span>
      <svg class="contact__icon" viewBox="0 0 24 24" aria-hidden="true" fill="none" stroke="#fff" stroke-width="1.6">
        <circle cx="12" cy="12" r="9"/>
        <ellipse cx="12" cy="12" rx="4" ry="9"/>
        <path d="M3 12 H21 M5 7 H19 M5 17 H19"/>
      </svg>
    </div>

    <div class="contact contact--email">
      <span>abc@halvernmail.example</span>
      <svg class="contact__icon" viewBox="0 0 24 24" aria-hidden="true">
        <rect x="2" y="5" width="20" height="14" fill="#fff"/>
        <path d="M2 5 L12 13 L22 5" fill="none" stroke="#3b3b3c" stroke-width="1.4"/>
      </svg>
    </div>
  </section>

</main>
</body>
</html>
```